Webbanner-Design
Zielgruppe
Verkauf von Pools und Zubehör
Aufgabenstellung
Es soll ein Banner für unseren Shop sein für eine Aktion, dass Holzpools jetzt sofort lieferbar sind Text:
Verschönern Sie doch Ihren Garten: Holzpools sofort lieferbar!
Unseren Shop finden Sie unter www.brisabad17.de
Fotos können von unserer Seite www.brisabad17-gallery.de verwendet werden
Das angefügte Bild sollte ebenfalls dabei sein. Hintergrund: die Leute sollen wegen Corona zu Hause bleiben und haben Zeit, daher sind unsere sofort lieferbaren Pools jetzt natürlich gut. Ich bin auch für abweichende Texte offen.

```html
<!DOCTYPE html>
<html lang="de">
<head>
<meta charset="utf-8">
<title>Brisabad17 – Holzpools sofort lieferbar</title>
<link href="https://fonts.googleapis.com/css2?family=Fira+Sans:wght@400;500&family=Barlow+Semi+Condensed:wght@600;700;800&display=swap" rel="stylesheet">
<style>
:root{
  --topbar:#12b8ea;
  --page:#ffffff;
  --outer:#ececec;
  --water-a:#0f7fc8;
  --water-b:#3fb4ea;
  --text:#333333;
  --muted:#555555;
  --line:#e2e2e2;
  --brand:#1b66b8;
  --banner-a:#0a93d8;
  --banner-b:#18b2ee;
  --navy:#0b1f7a;
  --deep:#0b3a8c;
}
*{box-sizing:border-box;margin:0;padding:0}
html,body{width:1200px;height:1023px;overflow:hidden}
body{background:var(--outer);font-family:"Fira Sans",sans-serif;color:var(--text);position:relative}
.water-backdrop{position:absolute;left:0;top:0;width:1200px;height:577px;
  background:radial-gradient(circle at 20% 30%,var(--water-b),transparent 60%),linear-gradient(160deg,var(--water-a),var(--water-b) 50%,var(--water-a))}
.page{position:absolute;left:99px;top:0;width:1002px;height:1023px;background:var(--page)}
.service-bar{height:32px;background:var(--topbar);display:flex;color:#fff;font-size:13px}
.service-bar .item{flex:1;display:flex;align-items:center;justify-content:center;gap:4px}
.service-bar svg{width:11px;height:11px}
.meta-links{position:absolute;right:27px;top:43px;display:flex;font-size:11px;color:var(--text)}
.meta-links span{padding:0 5px;border-left:1px solid var(--line)}
.meta-links span:first-child{border-left:none}
.brand{position:absolute;left:24px;top:88px;display:flex;align-items:center;gap:8px;font-size:26px;font-weight:500;color:var(--brand)}
.brand .dot{width:18px;height:18px;border-radius:50%;background:var(--brand)}
.search{position:absolute;left:548px;top:90px;width:222px;height:30px;border:1px solid #ccc;border-radius:3px;display:flex}
.search .field{flex:1;padding:6px 12px;font-size:13px;color:#999}
.search .btn{width:37px;border-left:1px solid #ccc;background:#f5f5f5;display:flex;align-items:center;justify-content:center}
.account,.cart{position:absolute;top:97px;font-size:13px;display:flex;align-items:center;gap:4px}
.account{left:795px}.cart{left:905px}
.caret{width:0;height:0;border-left:4px solid transparent;border-right:4px solid transparent;border-top:4px solid var(--text);margin-left:3px}
.main-nav{position:absolute;left:0;top:174px;width:1002px;height:45px;border-top:2px solid var(--line);border-bottom:2px solid var(--line);display:flex;align-items:center;padding-left:24px;gap:22px;font-size:13.5px;color:var(--muted)}
.main-nav span{display:flex;align-items:center}
.main-nav .caret{border-top-color:var(--muted);margin-left:2px}
.hero{position:absolute;left:20px;top:241px;width:962px;height:324px;overflow:hidden}
.hero svg.bg{position:absolute;left:0;top:0}
.hero .lead{position:absolute;left:49px;top:62px;font-family:"Barlow Semi Condensed",sans-serif;font-weight:700;font-size:31px;line-height:30px;color:#fff}
.hero .claim{position:absolute;left:49px;top:126px;font-family:"Barlow Semi Condensed",sans-serif;font-weight:800;font-size:51px;line-height:44px;color:var(--navy)}
.hero .shop-url{position:absolute;left:50px;top:278px;font-family:"Barlow Semi Condensed",sans-serif;font-weight:600;font-size:18px;color:#fff}
.badge-panel{position:absolute;left:333px;top:67px;width:191px;height:190px;background:var(--deep)}
.pager{position:absolute;left:0;width:1002px;top:591px;display:flex;justify-content:center;gap:16px}
.pager i{width:6px;height:6px;border-radius:50%;background:#444;margin-top:2px}
.pager i.on{width:10px;height:10px;margin-top:0;background:none;border:2px solid #444}
.divider{position:absolute;left:22px;right:22px;top:642px;border-top:1px solid var(--line)}
.section-title{position:absolute;left:22px;top:659px;font-size:22px;font-weight:400;color:var(--text)}
.category{position:absolute;top:756px;width:264px;text-align:center}
.category .photo{height:198px}
.category .name{margin-top:41px;font-size:13px;color:var(--text)}
</style>
</head>
<body>
<div class="water-backdrop" role="img" aria-label="Wasseroberfläche eines Pools"></div>
<div class="page">
  <div class="service-bar">
    <div class="item"><svg viewBox="0 0 12 12"><path d="M2 1l2 0 1 3-1.5 1a7 7 0 0 0 3.5 3.5L8 7l3 1v2a1 1 0 0 1-1 1A9 9 0 0 1 1 2a1 1 0 0 1 1-1z" fill="#fff"/></svg>+49 (0) 7391 / 846 317 2</div>
    <div class="item"><svg viewBox="0 0 12 12"><rect x="0.5" y="0.5" width="11" height="11" rx="2" fill="#fff"/><path d="M3 6l2 2 4-4" stroke="var(--topbar)" stroke-width="1.8" fill="none"/></svg>persönliche Beratung</div>
    <div class="item"><svg viewBox="0 0 12 12"><rect x="0.5" y="0.5" width="11" height="11" rx="2" fill="#fff"/><path d="M3 6l2 2 4-4" stroke="var(--topbar)" stroke-width="1.8" fill="none"/></svg>sicher Einkaufen</div>
    <div class="item"><svg viewBox="0 0 12 12"><circle cx="6" cy="6" r="6" fill="#fff"/><path d="M3 6h5M6 3.5L8.5 6 6 8.5" stroke="var(--topbar)" stroke-width="1.6" fill="none"/></svg>Brisabad-Galerie</div>
  </div>
  <nav class="meta-links"><span>Startseite</span><span>Mein Konto</span><span>Kontakt</span><span>Unsere Partner</span><span>Bildergalerie</span><span>Wir über uns</span><span>News</span></nav>
  <div class="brand"><span class="dot"></span>Brisabad17</div>
  <div class="search"><div class="field">Suchen</div><div class="btn"><svg width="15" height="15" viewBox="0 0 16 16"><circle cx="6.5" cy="6.5" r="5" stroke="var(--topbar)" stroke-width="2.2" fill="none"/><path d="M10.5 10.5l4 4" stroke="var(--topbar)" stroke-width="2.4"/></svg></div></div>
  <div class="account"><svg width="11" height="11" viewBox="0 0 12 12"><circle cx="6" cy="3.5" r="3" fill="#333"/><path d="M0.5 12a5.5 4.5 0 0 1 11 0z" fill="#333"/></svg>Anmelden<span class="caret"></span></div>
  <div class="cart"><svg width="13" height="11" viewBox="0 0 14 12"><path d="M0 1h2.5l2 7h7l2-5H4" stroke="#333" stroke-width="1.6" fill="#333"/><circle cx="5.5" cy="10.5" r="1.3" fill="#333"/><circle cx="10.5" cy="10.5" r="1.3" fill="#333"/></svg>0,00 €<span class="caret"></span></div>
  <nav class="main-nav"><span>Sonderangebote</span><span>Pool &amp; Zubehör<i class="caret"></i></span><span>Sauna<i class="caret"></i></span><span>Infrarot<i class="caret"></i></span><span>Holzbadewannen</span></nav>

  <section class="hero">
    <svg class="bg" width="962" height="324" viewBox="0 0 962 324">
      <defs>
        <linearGradient id="heroBlue" x1="0" y1="0" x2="1" y2="1"><stop offset="0" stop-color="var(--banner-b)"/><stop offset="1" stop-color="var(--banner-a)"/></linearGradient>
        <linearGradient id="gardenTone" x1="0" y1="0" x2="0" y2="1"><stop offset="0" stop-color="#b9c9d4"/><stop offset="0.35" stop-color="#6f8a4c"/><stop offset="0.6" stop-color="#3b86b4"/><stop offset="1" stop-color="#a8865a"/></linearGradient>
      </defs>
      <rect width="962" height="324" fill="url(#heroBlue)"/>
      <circle cx="40" cy="-20" r="110" fill="#2bbdf3" opacity="0.6"/>
      <circle cx="520" cy="330" r="60" fill="#2bbdf3" opacity="0.6"/>
      <polygon points="468,0 482,0 548,324 532,324" fill="var(--navy)"/>
      <polygon points="482,0 962,0 962,324 548,324" fill="url(#gardenTone)" role="img" aria-label="Foto eines eingelassenen Holzpools im Garten vor einem Haus"/>
    </svg>
    <div class="lead">VERSCHÖNERN SIE<br>DOCH IHREN GARTEN</div>
    <div class="claim">HOLZPOOLS<br>SOFORT<br>LIEFERBAR!</div>
    <div class="shop-url">www.brisabad17.de</div>
    <div class="badge-panel" role="img" aria-label="Platz für das Kampagnenabzeichen zum Zuhausebleiben"></div>
  </section>

  <div class="pager"><i></i><i class="on"></i><i></i><i></i><i></i></div>
  <div class="divider"></div>
  <h2 class="section-title">Unsere TOP-Kategorien</h2>

  <div class="category" style="left:42px"><div class="photo" role="img" aria-label="Achteckiger Holzpool auf Holzterrasse im Garten" style="background:linear-gradient(180deg,#6f9bc7 0%,#3e6b2e 30%,#4b7a32 55%,#9a7a4e 75%,#5f8f3a 100%)"></div><div class="name">Holzpools</div></div>
  <div class="category" style="left:369px"><div class="photo" role="img" aria-label="Blaue Poolabdeckung mit Stangen auf gepflastertem Rand" style="background:linear-gradient(90deg,#8a8a86 0%,#8a8a86 22%,#1f9ae6 25%,#2aa6ee 75%,#8a8a86 78%,#8a8a86 100%)"></div><div class="name">Poolabdeckungen</div></div>
  <div class="category" style="left:697px"><div class="photo" role="img" aria-label="Pool mit Rollabdeckung und Steinplattenrand" style="background:linear-gradient(160deg,#2f3a2c 0%,#a9bccc 30%,#3c7fd0 60%,#8d8a84 80%,#6d6a64 100%)"></div><div class="name">Oberflur</div></div>
</div>
</body>
</html>
```